Simple, Professional and neat business card design for Vendralo Inc.

We're looking to re-vamp our business card design. We're a supplier of innovative feed ingredients for the North American animal agriculture industry. We are located in Lucknow, Ontario, Canada and our flagship product is a product that prevents milk fever in dairy cows when the calve, it is fed before calving and is very effective compared to other alternatives available on the market today.

Our company has Danish roots and we import all of our product from our Danish partner/manufacturer in Denmark. We like our design to embrace high professionalism while remaining neat and simple.

Target Market(s)

B2B, Feed Mills, Veterinary Clinics, Large integrators/producers,

Industry/Entity Type

Agribusiness

Contact Information for Business Card

We like the rounded corners because they make the card easy to sit in a wallet and not many use it so it makes the card stand out, just possibly something to take account for during the design.

As you can also see on the sliders below, looking for a that simple but proffesional scandinavian design.

Requirements
Nice to have
• Rounded corners
Should not have
• Too vibrant

```html
<!DOCTYPE html>
<html lang="en">
<head>
<meta charset="utf-8">
<title>Vendralo Inc. – Business Card</title>
<link href="https://fonts.googleapis.com/css2?family=Poppins:wght@400;500;600;700;800&display=swap" rel="stylesheet">
<style>
  :root {
    --backdrop: #1b1b1b;
    --card-green: #74b441;
    --card-green-edge: #5f9a34;
    --card-green-light: #7dbb46;
    --bracket-gold: #e3c98e;
    --brand-blue: #0e56a8;
    --text-white: #ffffff;
    --label-dark: #1a2410;
  }
  * { box-sizing: border-box; margin: 0; padding: 0; }
  html, body {
    width: 994px; height: 1200px; overflow: hidden;
    background: var(--backdrop);
    font-family: "Poppins", sans-serif;
  }
  .canvas { position: relative; width: 994px; height: 1200px; }
  .card {
    position: absolute; left: 124px; width: 746px; height: 426px;
    border-radius: 8px; overflow: hidden;
    background:
      radial-gradient(ellipse at center, var(--card-green-light) 0%, var(--card-green) 60%, var(--card-green-edge) 100%);
    box-shadow: 0 6px 18px rgba(0,0,0,0.45);
  }
  .card--front { top: 124px; }
  .card--back { top: 650px; }
  .corner-brackets { position: absolute; inset: 0; width: 746px; height: 426px; }
  .brand-lockup {
    position: absolute; left: 0; right: 0; top: 300px; transform: translateY(-50%);
    display: flex; align-items: center; justify-content: center; gap: 22px;
  }
  .brand-mark {
    width: 72px; height: 72px; border-radius: 50%; background: var(--brand-blue);
  }
  .brand-name {
    font-weight: 700; font-size: 58px; letter-spacing: -1.5px;
    color: var(--brand-blue); line-height: 1;
  }
  .website {
    position: absolute; left: 0; right: 0; top: 388px;
    text-align: center; color: var(--text-white); font-size: 16px; font-weight: 500;
  }
  .person-name {
    position: absolute; left: 0; right: 0; top: 58px;
    text-align: center; color: var(--text-white);
    font-size: 47px; font-weight: 800; letter-spacing: -0.5px;
    text-shadow: 1px 2px 2px rgba(0,0,0,0.35);
  }
  .name-rule {
    position: absolute; left: 173px; width: 401px; top: 139px;
    border-top: 1px dashed rgba(255,255,255,0.75);
  }
  .contact-block {
    position: absolute; left: 0; right: 0; text-align: center;
  }
  .contact-label {
    color: var(--label-dark); font-size: 13px; font-weight: 500; letter-spacing: 0.2px;
    line-height: 18px;
  }
  .contact-value {
    color: var(--text-white); font-size: 16px; font-weight: 400; line-height: 21px;
    margin-top: 4px;
  }
  .contact-value + .contact-value { margin-top: 0; }
  .contact-block--email { top: 170px; }
  .contact-block--phone { top: 235px; }
  .contact-block--address { top: 316px; }
</style>
</head>
<body>
<div class="canvas">

  <section class="card card--front">
    <svg class="corner-brackets" viewBox="0 0 746 426" aria-hidden="true">
      <g fill="none" stroke="var(--bracket-gold)" stroke-width="1.5">
        <polyline points="66,22 22,22 22,66"/>
        <polyline points="680,22 724,22 724,66"/>
        <polyline points="22,361 22,404 66,404"/>
        <polyline points="724,361 724,404 680,404"/>
      </g>
    </svg>
    <div class="brand-lockup">
      <span class="brand-mark"></span>
      <span class="brand-name">VENDRALO INC.</span>
    </div>
    <p class="website">www.vendralo.com</p>
  </section>

  <section class="card card--back">
    <svg class="corner-brackets" viewBox="0 0 746 426" aria-hidden="true">
      <g fill="none" stroke="var(--bracket-gold)" stroke-width="1.5">
        <polyline points="66,22 22,22 22,66"/>
        <polyline points="680,22 724,22 724,66"/>
        <polyline points="22,361 22,404 66,404"/>
        <polyline points="724,361 724,404 680,404"/>
      </g>
    </svg>
    <h1 class="person-name">MIKKEL ANDERSEN</h1>
    <div class="name-rule"></div>

    <div class="contact-block contact-block--email">
      <p class="contact-label">EMAIL ADDRESS</p>
      <p class="contact-value">mikkel@vendralo.com</p>
    </div>

    <div class="contact-block contact-block--phone">
      <p class="contact-label">TELEPHONE</p>
      <p class="contact-value">Mobile: 519-555-0148, Office: 519-555-0172</p>
      <p class="contact-value">Toll Free: 888-555-0190, Fax: 519-555-0199</p>
    </div>

    <div class="contact-block contact-block--address">
      <p class="contact-label">ADDRESS</p>
      <p class="contact-value">Box 412, Westford, Ontario Canada N0X 1A0</p>
    </div>
  </section>

</div>
</body>
</html>
```